Brightwater Subsea Systems Alliance

Hi, I am having a workshop at the beginning of June on the above topic and require the following:
I would like the following:
- PPT template in widescreen and regular format (these are really the same but just need but design just needs to be scalable). I like clean ppt templates showing the section but leaving much of the slide for actual content. I like clean no nonsense fonts (calibri, arial, etc)
- 3 fold brochure (stationary)
- poster template for 8.5"x11" and 11"x17" posters (stationary, I do not need a letterhead per se except for the workshop agenda.
- The added stationary and logo options I picked on the "Design Options" page should cover all of the above.

It is not for the https://tidewellhub.ca/ but we are an academic led network from www.halvardcol.ca wanting to do collaborate and do work in the key areas of the Tidewell Hub especially related to offshore oil and gas in the areas of: production optimization, automation, safety & risk, marine operations, communications and controls, human factors, remote leadership an teams.

Keywords: digital oilfield, offshore oil and gas, integrated operations, digitalization, TAX47, Ravnholt digital oil and gas, integrated operations, remote and harsh (ice and icebergs) offshore oil and gas field development, automation in oil and gas

I am hoping that since its just a workshop and the development needs to be done within the halvardcol.ca/pubrel/site/PKguide/ framework, so its really just a banner and/or the ppt/poster graphic can fit within the HVC Page Kit template. The creation we will do.

Giving an extension until tomorrow. Based on what I see now, we will need to work together a little bit to get what I want/need. Okay?

1 page

Serif
Sans Serif

3176b5
33a6d7
33b8a4

```html
<!DOCTYPE html>
<html lang="en">
<head>
<meta charset="utf-8">
<title>Brightwater Subsea Systems Alliance – Slide Templates</title>
<link href="https://fonts.googleapis.com/css2?family=Open+Sans:wght@600&display=swap" rel="stylesheet">
<style>
  :root {
    --stage: #3d3d3d;
    --brand-blue: #3176b5;
    --brand-sky: #33a6d7;
    --brand-teal: #33b8a4;
    --sea-warm: #f3e6d6;
    --sea-haze: #dfe3e6;
    --sea-deep: #2f6f8e;
    --sea-dark: #1f4f6b;
    --mist-light: #f2f2f2;
    --mist-mid: #dcdcdc;
  }
  * { margin: 0; padding: 0; box-sizing: border-box; }
  html, body {
    width: 1200px; height: 1000px; overflow: hidden;
    background: var(--stage);
    font-family: "Open Sans", Arial, sans-serif;
  }
  .canvas { position: relative; width: 1200px; height: 1000px; }
  .slide { position: absolute; overflow: hidden; }

  .slide--title { left: 249px; top: 50px; width: 733px; height: 412px; }
  .slide--title .photo {
    position: absolute; inset: 0;
    background: linear-gradient(180deg,
      var(--sea-warm) 0%, #f6eadc 22%, var(--sea-haze) 38%,
      #6fa3bd 48%, var(--sea-deep) 62%, var(--sea-dark) 78%, #6f8fa3 92%, #c9b9a8 100%);
  }
  .slide--title .shapes { position: absolute; inset: 0; }

  .slide--content { left: 249px; top: 535px; width: 737px; height: 415px; }
  .slide--content .photo {
    position: absolute; left: 0; top: 0; width: 100%; height: 402px;
    background: linear-gradient(180deg,
      var(--mist-mid) 0%, #e6e6e6 35%, #f0f0f0 48%, var(--mist-light) 60%,
      #e2e2e2 65%, #ececec 68%, var(--mist-light) 100%);
  }
  .slide--content .rule-blue {
    position: absolute; left: 0; top: 402px; width: 100%; height: 6px; background: var(--brand-blue);
  }
  .slide--content .rule-teal {
    position: absolute; left: 0; top: 408px; width: 100%; height: 7px; background: var(--brand-teal);
  }

  .brand {
    position: absolute; width: 72px;
    display: flex; align-items: flex-start; gap: 3px;
    color: var(--brand-blue); font-weight: 600;
    font-size: 6.5px; line-height: 1.25; text-transform: uppercase; letter-spacing: 0.2px;
  }
  .brand__mark { flex: 0 0 8px; height: 8px; background: var(--brand-blue); margin-top: 1px; }
  .slide--title .brand { right: 18px; top: 16px; }
  .slide--content .brand { right: 12px; bottom: 26px; }
</style>
</head>
<body>
<main class="canvas">
  <section class="slide slide--title">
    <div class="photo" role="img" aria-label="Close-up photograph of ocean waves at sunrise with rocks and distant mountains"></div>
    <svg class="shapes" width="733" height="412" viewBox="0 0 733 412" aria-hidden="true">
      <polygon points="0,0 339,0 102,412 0,412" fill="var(--brand-blue)"/>
      <polygon points="102,412 155,322 241,412" fill="var(--brand-teal)"/>
    </svg>
    <div class="brand"><span class="brand__mark"></span><span>Brightwater Subsea Systems Alliance</span></div>
  </section>

  <section class="slide slide--content">
    <div class="photo" role="img" aria-label="Faded grey photograph of an offshore horizon with wind turbines under a cloudy sky"></div>
    <div class="rule-blue"></div>
    <div class="rule-teal"></div>
    <div class="brand"><span class="brand__mark"></span><span>Brightwater Subsea Systems Alliance</span></div>
  </section>
</main>
</body>
</html>
```